Tri-fold Brochure for a Massage Therapist Specializing in Injury Treatment

I need your help to make this brochure beautiful. It's 8 1/2" x 11", full color, two-sided, tri-fold.

It will be primarily distributed in medical clinics, so it should be visually attractive to people who are awaiting treatment for injuries sustained in a motor vehicle accident.

Motor vehicle accident claims are only one sub-section of my total clientele, so this is a specifically targeted campaign. However, I also have many clients that I see regularly as an ongoing part of their personal health and wellness regimen. These clients tend to have above-average incomes, and I would like this particular brochure to have some cross-over appeal to that market as well, if possible.

The plain text version of the two-sided design is attached. Both pages are already divided into thirds along the fold lines. Feel free to get creative with font sizing and spacing to accommodate graphics as long as the text within each folded section remains within that section.

I don't have an official logo, but I have been using the water droplet image (on the back of the brochure) on my web and print materials. It doesn't necessarily need to be included, but it would be nice for the sake of consistency. I'm attaching a copy of the droplet as well as a version that shows the style of font I've been using in other forms of print advertising.

Just FYI: I am a sole proprietor and my legal business name is my name - Marla J. Densford, LMP. "Gentle Tissue Care & Steady Recovery Massage" started out as more of a tag line, but has evolved into the non-official name of my business.

Thanks in advance for your help!

Target Market(s)

Women & men of all ages that have been injured in a motor vehicle accident.

Industry/Entity Type

Health Care

Font styles to use
Serif
Other font styles liked:
• KennedyCapsDB_Normal

Requirements
Must have
• Text content should remain as written. Brochure text within each folded section should remain within that section.
• I'm open to suggestions, though. And if you notice any typos, please let me know!
Nice to have
• Water drop image near my name on the back side would be nice to include, but it's not absolutely necessary.
• I personally prefer colors in shades of blue & green, but I look forward to seeing what the designers choose.
Should not have
• I am very particular about stock photos that represent massage therapy. I prefer photos that represent the way I work with my injured clients, so this excludes the strictly "spa-type" images such as beautiful half-naked women with flowers in their hair and warm stones placed along their spine.
• Also, I only do table massage; no chair massage. So stock photos showing patients seated in specially designed portable massage chairs should not be used.
• Photos should be more clinical in nature, not picture the therapist other than their arms & hands (which should be female), and not picture the patient's exposed hips or side of the breast. All draping of the patient's body (male or female) must be complete & secure - no towels, tube tops, or bikinis.
• I would prefer that any photos of the therapist's hands look similar to mine, which are female, petite, and fair skinned without freckles. The skin tone of the pictured patient does not matter.
• If the patient is pictured face down, they need to be using the table's face cradle, not with their head turned to either side. (Anyone with whiplash would look at a photo like that and just see pain!) Likewise, the therapist's action should not look painful, so no photos of deep tissue techniques involving knuckles, elbows, or uncomfortable body positioning.
• The majority of my injured patients have lower back, upper back, neck and shoulder pain, so pictures that feature these areas (in the way I've outlined above) would be preferred.
• If you have any questions about photos, please don't hesitate to ask!

```html
<!DOCTYPE html>
<html lang="en">
<head>
<meta charset="utf-8">
<title>Effective Therapy – Marla J. Densford, LMP</title>
<link rel="stylesheet" href="https://fonts.googleapis.com/css2?family=PT+Serif:ital,wght@0,400;0,700;1,400;1,700&family=Libre+Baskerville:ital,wght@1,700&display=swap">
<style>
  :root{
    --sky:#0c9ad8;
    --sky-deep:#0886c6;
    --navy:#0b5a96;
    --navy-dark:#094a80;
    --band-light:#1f93d2;
    --ink-blue:#2767a3;
    --bullet-blue:#1c568c;
    --mist:#e6f2fa;
    --white:#ffffff;
  }
  *{box-sizing:border-box;margin:0;padding:0}
  html,body{width:1200px;height:848px;overflow:hidden;background:#fff}
  .brochure{position:relative;width:1200px;height:848px;overflow:hidden;background:var(--white);font-family:"PT Serif",Georgia,serif}

  .backdrop{position:absolute;inset:0;width:1200px;height:848px}

  /* Left panel */
  .panel-intro{position:absolute;left:0;top:0;width:402px;height:610px;
    background:linear-gradient(160deg,var(--sky) 0%,var(--sky-deep) 100%);
    color:var(--white);padding:27px 28px 0 27px;font-size:14px;line-height:18.5px;letter-spacing:-0.1px}
  .panel-intro p{margin-bottom:8.5px}
  .panel-intro strong{font-weight:700}
  .intro-band{position:absolute;left:0;top:610px;width:402px;height:16px;background:var(--navy)}
  .photo-intro{position:absolute;left:0;top:626px;width:402px;height:222px;
    background:linear-gradient(100deg,#d9d2cc 0%,#b79a88 35%,#8a6f63 55%,#c7b3a8 75%,#e3a94a 90%,#5b86b8 100%)}

  /* Header band */
  .header-band{position:absolute;left:402px;top:0;width:798px;height:76px;background:var(--navy)}
  .header-strip{position:absolute;left:402px;top:76px;width:798px;height:14px;background:var(--band-light)}
  .title{position:absolute;left:436px;top:30px;font-family:"Libre Baskerville",Georgia,serif;font-style:italic;font-weight:700;font-size:27px;color:var(--white);letter-spacing:.2px}
  .practitioner{position:absolute;right:18px;top:38px;font-family:"PT Serif",Georgia,serif;font-weight:400;font-size:22px;line-height:26px;color:var(--white);white-space:nowrap}
  .practitioner small{font-size:15px}

  .photo-therapy{position:absolute;left:402px;top:90px;width:394px;height:150px;
    background:linear-gradient(90deg,#3b4f6a 0%,#55657a 22%,#e7c3ad 40%,#f0d3c1 65%,#f4f5f7 85%,#e9edf1 100%)}

  .portrait-ring{position:absolute;left:812px;top:8px;width:148px;height:148px;border-radius:50%;background:var(--navy);padding:5px}
  .portrait{width:100%;height:100%;border-radius:50%;border:3px solid var(--white);
    background:radial-gradient(circle at 50% 45%,#e9c0a6 0%,#c98a6c 45%,#7f3d2c 75%,#3f4c48 100%)}

  /* Middle panel */
  .panel-benefits{position:absolute;left:433px;top:264px;width:350px;color:var(--ink-blue);font-size:14px;line-height:18.5px}
  .panel-benefits p{margin-bottom:8.5px}
  .benefit-list{list-style:none;margin-top:8px}
  .benefit-list li{position:relative;padding-left:13px;height:27px;font-family:"Libre Baskerville",Georgia,serif;font-style:italic;font-weight:700;font-size:13px;color:var(--bullet-blue)}
  .benefit-list li::before{content:"•";position:absolute;left:0;top:0;font-style:normal}

  /* Right panel */
  .panel-about{position:absolute;left:830px;top:97px;width:346px;color:var(--ink-blue);font-size:14px;line-height:18.5px}
  .panel-about p{margin-bottom:8.5px}
  .panel-about .wrap{display:block}

  .photo-care{position:absolute;left:0;top:0;width:1200px;height:848px}
</style>
</head>
<body>
<div class="brochure">

  <svg class="backdrop" viewBox="0 0 1200 848" aria-hidden="true">
    <path d="M620 848 C640 560 820 360 1200 300 L1200 330 C860 390 690 580 680 848 Z" fill="#eef6fb"/>
    <path d="M700 300 C860 320 1040 380 1200 470 L1200 848 L1020 848 C1000 600 880 420 700 300 Z" fill="#f2f8fc"/>
  </svg>

  <section class="panel-intro">
    <p>According to the automotive insurance industry’s statistics, more than 2 million people are injured in car accidents every year.</p>
    <p>If you are one of these people, you may be surprised to know that the Personal Injury Protection (PIP) coverage of your auto insurance policy will pay for you to receive massage therapy for your injuries. Why? Insurance companies know that <strong>massage therapy reduces pain and shortens the total recovery time after an injury.</strong></p>
    <p>In an instant, a collision can cause profound damage to your musculoskeletal system, and the results are not always immediately felt. Thanks to your body’s natural defense mechanisms – including an immediate rush of adrenaline – you might not feel the effects of the impact until the shock wears off and your body begins to process the damage. Hours, days, weeks, or even months may pass before the full effects are realized.</p>
    <p><strong>A minor accident can have a major impact on your health for years to come.</strong> In fact, an impact at just 5 mph can be enough to cause a whiplash injury, chronic headaches, sciatica, and significant bodily pain, particularly in the back, shoulder, knee, or hip, in addition to a host of other potential health issues.</p>
    <p>If you or someone you care about has been involved in a motor vehicle accident, the first step on the path to optimal wellness is a visit to a physician for an examination and prescription for massage therapy.</p>
  </section>
  <div class="intro-band"></div>
  <div class="photo-intro" role="img" aria-label="Photo of a woman holding her sore neck in pain"></div>

  <div class="header-band"></div>
  <div class="header-strip"></div>
  <h1 class="title">Effective Therapy</h1>
  <div class="photo-therapy" role="img" aria-label="Photo of a therapist's hands massaging a draped patient's lower back"></div>

  <div class="portrait-ring"><div class="portrait" role="img" aria-label="Portrait photo of the massage practitioner"></div></div>
  <h2 class="practitioner">Marla J. Densford, <small>LMP</small></h2>

  <section class="panel-benefits">
    <p>Massage therapy is well known for its ability to promote a deep sense of relaxation. However, the benefits extend far beyond simply feeling relaxed. Multiple research studies have conclusively proven the positive health benefits of therapeutic massage, particularly its effectiveness for injury rehabilitation.</p>
    <p>One recent study at Harwick University found that just 10 minutes of massage therapy not only caused a reduction in muscle tension and pain, but also triggered a biochemical response that reduced inflammation and promoted cellular repair in damaged muscle tissue, speeding the healing process.</p>
    <p>Therapeutic massage has been proven to aid rehabilitation by:</p>
    <ul class="benefit-list">
      <li>Reducing pain</li>
      <li>Reducing stress &amp; muscle tension</li>
      <li>Relieving muscle spasms</li>
      <li>Reducing frequency &amp; duration of headaches</li>
      <li>Improving flexibility &amp; range of motion in joints</li>
      <li>Decreasing swelling &amp; improving circulation</li>
      <li>Enhancing quality of sleep</li>
      <li>Decreasing anxiety &amp; depression</li>
      <li>Shortening recovery time</li>
    </ul>
  </section>

  <section class="panel-about">
    <p>
      <span class="wrap" style="padding-left:142px">Since my initial certification as a</span>
      <span class="wrap" style="padding-left:134px">Licensed Massage Practitioner in</span>
      <span class="wrap" style="padding-left:128px">1997, I’ve continued to pursue</span>
      <span class="wrap" style="padding-left:106px">advanced training in multiple</span>
      bodywork modalities, including Myofascial Release, Neuromuscular Therapy, Manual Lymphatic Drainage, injury-specific deep tissue techniques, and many more.
    </p>
    <p>In my private practice I’ve had the opportunity to work with people of all ages, from infants to seniors, in a variety of settings from upscale spas and health clubs to medical clinics and rehabilitation centers. All of this has influenced my unique bodywork style.</p>
    <p>Multiple techniques are incorporated into each massage session, determined by the specific injuries involved, as well as your personal preferences and treatment goals.&nbsp; I believe very strongly that effective treatment work should also be as relaxing as possible, and I strive to combine the science of a clinically-focused therapeutic approach with the flowing artistry of a soothing spa experience – all in the comfort of your own home or office.</p>
    <p>My ultimate goal is to leave you feeling more relaxed, balanced, and rejuvenated, with a deeper understanding of your own body. It is in this state that the most profound healing can occur.</p>
  </section>

  <svg class="photo-care" viewBox="0 0 1200 848">
    <defs>
      <linearGradient id="careTone" x1="0" y1="0" x2="1" y2="1">
        <stop offset="0" stop-color="#f3eee9"/>
        <stop offset=".45" stop-color="#f0c9b2"/>
        <stop offset=".75" stop-color="#e9b89e"/>
        <stop offset="1" stop-color="#dcdfe3"/>
      </linearGradient>
    </defs>
    <path d="M690 848 C730 700 900 620 1200 612 L1200 848 Z" fill="var(--band-light)"/>
    <path d="M712 848 C760 710 920 636 1200 628 L1200 848 Z" fill="var(--navy)"/>
    <path d="M726 848 C776 720 930 648 1200 642 L1200 848 Z" fill="url(#careTone)" role="img" aria-label="Photo of a therapist's hands supporting a patient's foot and ankle"/>
  </svg>

</div>
</body>
</html>
```